The Lantern Assembly Pitchdeck Template

The Lantern Assembly would like a branded pitch deck template design for members to use when presenting their projects and proposals. The deck should include 10-15 different slide designs, each with the same branded theme, but with a variety of icon graphics and other design features that will empower members to easily create a beautiful pitch deck just by adding written content.

Please visit thelantern.org to get a sense for our branding - purple, space, galaxy, white font and the planetary logo are some commonalities.

Here are 2 google drive links with some additional designs

https://files.cloudnestbox.net/share/u/1/dir/8KpqZr3Tn5Yb-wLxVd2Hc-Qm4jEsAf7Ug

https://files.cloudnestbox.net/share/u/1/dir/6Rtb2-Lm9Xc4-hNwq813Fvkzpe_Jd7Sa

```html
<!DOCTYPE html>
<html lang="en">
<head>
<meta charset="utf-8">
<title>The Lantern Assembly – Pitch Deck Template</title>
<link href="https://fonts.googleapis.com/css2?family=Questrial&family=Mulish:wght@400;700&display=swap" rel="stylesheet">
<style>
  :root{
    --page:#ffffff;
    --slide:#1c1c1e;
    --slide-deep:#141416;
    --ink:#ffffff;
    --ink-soft:#d9d6e4;
    --ink-dim:#9a97a6;
    --violet:#6a1fd1;
    --violet-deep:#3a0fa0;
    --indigo:#2a0f8f;
    --magenta:#c13adf;
    --orchid:#9a3ad8;
    --silver:#b8b8bc;
  }
  *{box-sizing:border-box;margin:0;padding:0}
  html,body{width:1088px;height:1200px;overflow:hidden;background:var(--page)}
  body{font-family:"Questrial",sans-serif;color:var(--ink)}
  .canvas{position:relative;width:1088px;height:1200px}
  .slide{position:absolute;width:338px;height:190px;background:var(--slide);overflow:hidden}
  .abs{position:absolute}
  .c1{left:25px}.c2{left:376px}.c3{left:727px}
  .r1{top:49px}.r2{top:273px}.r3{top:497px}.r4{top:723px}.r5{top:948px}

  .heading{position:absolute;left:14px;top:9px;font-size:11px;font-weight:400;letter-spacing:.2px;text-transform:uppercase;white-space:nowrap}
  .heading::after{content:"";position:absolute;left:0;top:15px;width:30px;height:1.5px;background:var(--ink)}
  .heading.right{left:auto;right:12px}
  .heading.right::after{left:auto;right:0}
  .heading.center{left:0;right:0;text-align:center}
  .heading.center::after{left:50%;margin-left:-15px}
  .heading.script{text-transform:none}

  .footer{position:absolute;left:0;right:0;bottom:0;height:10px;background:var(--slide-deep);font-family:"Mulish",sans-serif}
  .footer .page{position:absolute;left:6px;top:1px;font-size:4.5px;color:var(--ink-dim)}
  .footer .page b{font-size:7px;color:var(--ink);font-weight:400;margin-left:3px}
  .footer .url{position:absolute;left:0;right:0;top:2.5px;text-align:center;font-size:4.5px;color:var(--ink-soft)}
  .footer .url.left{right:auto;left:132px}
  .footer .mark{position:absolute;right:6px;top:1.5px;font-family:"Questrial",sans-serif;font-size:6px;color:var(--ink)}

  .brand-name{font-size:17px;letter-spacing:.2px;line-height:1;font-weight:400;white-space:nowrap}
  .brand-tag{font-size:7.5px;letter-spacing:.1px;margin-top:4px;white-space:nowrap}
  .rule{height:1.2px;background:var(--ink)}

  .photo{position:absolute}
  .body-copy{font-family:"Mulish",sans-serif;color:var(--ink)}
  .item-title{font-family:"Mulish",sans-serif;font-weight:700;font-size:6px;text-align:center}
  .item-text{font-family:"Mulish",sans-serif;font-size:4.4px;line-height:1.35;color:var(--ink);margin-top:2px}

  .diamond{position:absolute;width:13px;height:13px;transform:rotate(45deg);background:linear-gradient(135deg,var(--magenta),var(--violet-deep))}
  .chip{position:absolute;width:15px;height:15px;border-radius:50%;background:linear-gradient(135deg,var(--orchid),var(--indigo));border:1px solid #ffffff55}

  .card-dark{position:absolute;background:#0f0f12;border:1px solid #ffffffaa;border-radius:6px;text-align:center;padding:4px 5px}
  .card-dark h4{font-size:5.5px;font-weight:400;margin:2px 0 2px}
  .card-dark p{font-family:"Mulish",sans-serif;font-size:3.4px;line-height:1.3;text-align:justify;color:var(--ink-soft)}

  .tile{position:absolute;width:59px;height:61px;border-radius:5px;border:1px solid #55555c;background:#121214;display:flex;align-items:center;justify-content:center}
</style>
</head>
<body>
<main class="canvas">

  <section class="slide c1 r1">
    <div class="photo" role="img" aria-label="Night sky photo of a rock arch under the Milky Way with a lone figure" style="inset:0;background:radial-gradient(ellipse at 62% 55%,#6a4c6e 0%,#2a1f2c 30%,#121015 65%),linear-gradient(#1a1820,#0c0b0e)"></div>
    <div class="abs rule" style="left:19px;top:74px;width:1.2px;height:33px"></div>
    <div class="abs" style="left:24px;top:76px">
      <div class="brand-name">THE LANTERN</div>
      <div class="brand-tag">UNITING HUMANITY AS ONE</div>
    </div>
  </section>

  <section class="slide c2 r1" style="background:#000">
    <div class="photo" role="img" aria-label="Green and teal nebula sky with a silhouetted man holding his arms wide" style="inset:0;background:radial-gradient(ellipse at 62% 20%,#2f6f62 0%,#173a3a 30%,transparent 60%),radial-gradient(ellipse at 80% 70%,#1e3e4a 0%,transparent 55%),linear-gradient(90deg,#000 0%,#000 25%,#061014 55%,#0a1c22 100%)"></div>
    <div class="abs" style="left:24px;top:94px">
      <div class="brand-name">THE LANTERN</div>
      <div class="brand-tag">UNITING HUMANITY AS ONE</div>
    </div>
    <div class="abs" style="left:22px;top:133px;width:128px;height:1px;background:linear-gradient(90deg,transparent,#fff,transparent)"></div>
  </section>

  <section class="slide c3 r1">
    <div class="abs" style="left:18px;top:94px">
      <div class="brand-name">THE LANTERN</div>
      <div class="brand-tag">UNITING HUMANITY AS ONE</div>
    </div>
    <div class="abs rule" style="left:17px;top:132px;width:146px"></div>
    <svg class="abs" style="left:0;top:0" width="338" height="190" viewBox="0 0 338 190">
      <defs>
        <linearGradient id="tri-sky" x1="0" y1="0" x2="0" y2="1">
          <stop offset="0" stop-color="#7a4f8e"/><stop offset=".5" stop-color="#c98a6a"/><stop offset="1" stop-color="#1b2240"/>
        </linearGradient>
      </defs>
      <polygon points="210,190 250,150 264,0 338,60 338,190" fill="#10131f" role="img" aria-label="Deep starfield behind the frame"/>
      <polygon points="264,0 298,120 226,120" fill="url(#tri-sky)" role="img" aria-label="Milky Way sky over a lone figure, cut into a triangle"/>
      <polyline points="196,190 196,46 240,100 264,0" fill="none" stroke="var(--silver)" stroke-width="5"/>
      <polyline points="264,0 338,8 338,160 300,110" fill="none" stroke="#8d8d92" stroke-width="5"/>
    </svg>
  </section>

  <section class="slide c1 r2">
    <div class="photo" role="img" aria-label="Sunset over the sea with a man raising his arms inside a faint planet ring" style="left:0;top:0;width:338px;height:120px;background:linear-gradient(#262028 0%,#4a3f48 50%,#b08a68 78%,#3a3440 100%)"></div>
    <div class="abs" style="left:62px;top:138px">
      <div class="brand-name" style="font-size:18px">THE LANTERN</div>
      <div class="brand-tag">UNITING HUMANITY AS ONE</div>
    </div>
    <div class="abs rule" style="left:195px;top:125px;width:1.2px;height:60px"></div>
    <p class="abs body-copy" style="left:204px;top:135px;width:126px;font-size:4px;line-height:1.3">Lorem ipsum dolor sit amet, consectetur adipiscing elit, sed do eiusmod tempor incididunt ut labore et dolore magna aliqua. Ut enim ad minim veniam, quis nostrud exercitation ullamco laboris nisi ut aliquip ex ea commodo consequat. Duis aute irure dolor in reprehenderit in voluptate velit esse cillum dolore eu fugiat nulla pariatur.</p>
  </section>

  <section class="slide c2 r2">
    <div class="photo" role="img" aria-label="Purple galaxy band" style="left:0;top:0;width:338px;height:89px;background:radial-gradient(ellipse at 60% 70%,#8b4fe0 0%,transparent 55%),linear-gradient(160deg,#5a1aa8,#2c0f7a 60%,#4a1898)"></div>
    <h2 class="heading script">Welcome Message</h2>
    <div class="photo" role="img" aria-label="Portrait photo of the speaker" style="left:137px;top:51px;width:66px;height:66px;border-radius:50%;border:2.5px solid #fff;background:linear-gradient(#e9e9ec,#9a9aa2)"></div>
    <div class="abs" style="left:22px;top:106px;font-family:Georgia,serif;font-size:20px;font-weight:700;line-height:1">&ldquo;</div>
    <p class="abs body-copy" style="left:22px;top:126px;width:298px;font-size:4.4px;line-height:1.35">Lorem ipsum dolor sit amet, consectetur adipiscing elit, sed do eiusmod tempor incididunt ut labore et dolore magna aliqua. Ut enim ad minim veniam, quis nostrud exercitation ullamco laboris nisi ut aliquip ex ea commodo consequat. Duis aute irure dolor in reprehenderit in voluptate velit esse cillum dolore eu fugiat nulla pariatur. Excepteur sint occaecat cupidatat non proident, sunt in culpa qui officia</p>
    <div class="abs" style="left:152px;top:155px;font-family:Georgia,serif;font-size:20px;font-weight:700;line-height:1">&rdquo;</div>
    <footer class="footer"><span class="page">Page No:<b>01</b></span><span class="url">https://www.thelantern.org/</span><span class="mark">Lantern</span></footer>
  </section>

  <section class="slide c3 r2">
    <h2 class="heading">What we envision</h2>
    <div class="abs" style="left:0;top:51px;width:338px;height:64px;background:linear-gradient(90deg,var(--violet),var(--indigo) 60%,var(--violet-deep))"></div>
    <div class="photo" role="img" aria-label="Child lying in autumn leaves" style="left:22px;top:34px;width:85px;height:101px;border-radius:0 0 0 14px;background:linear-gradient(140deg,#7a3a1e,#a86a30 45%,#3a6a62 70%,#5a2a16)"></div>
    <div class="photo" role="img" aria-label="Hands holding planet Earth" style="left:124px;top:34px;width:85px;height:101px;border-radius:14px 0 14px 0;background:radial-gradient(circle at 48% 28%,#5b7fb0 0%,#2a3a5a 14%,#0a0a0c 30%),linear-gradient(#0a0a0c 50%,#6a2e1c)"></div>
    <div class="photo" role="img" aria-label="Dove released from a hand against a sunset" style="left:230px;top:34px;width:85px;height:101px;border-radius:0 14px 0 0;background:radial-gradient(circle at 55% 65%,#ffe58a 0%,#f2a33a 30%,#c0306a 75%,#8a1f6a)"></div>
    <div class="abs" style="left:22px;top:141px;width:85px;text-align:center;font-size:6px">PEOPLE</div>
    <div class="abs" style="left:124px;top:141px;width:85px;text-align:center;font-size:6px">PLANET</div>
    <div class="abs" style="left:230px;top:141px;width:85px;text-align:center;font-size:6px">PEACE</div>
    <p class="abs body-copy" style="left:28px;top:150px;width:72px;font-size:3.5px;line-height:1.3">A World that meets the needs of every human being as a birth right, providing the foundation for self-actualization.</p>
    <p class="abs body-copy" style="left:131px;top:150px;width:72px;font-size:3.5px;line-height:1.3">A World that lives in harmony with Nature; restore and protect Mother Earth, including the Animal Kingdom.</p>
    <p class="abs body-copy" style="left:237px;top:150px;width:72px;font-size:3.5px;line-height:1.3">A World that chooses peace, love and harmony, awake and aware of its connection with everything.</p>
    <footer class="footer"><span class="page">Page No:<b>02</b></span><span class="url">https://www.thelantern.org/</span><span class="mark">Lantern</span></footer>
  </section>

  <section class="slide c1 r3">
    <h2 class="heading">Our Mission</h2>
    <div class="abs" style="left:216px;top:0;width:28px;height:101px;background:linear-gradient(var(--violet-deep),var(--violet))"></div>
    <div class="photo" role="img" aria-label="Man on a rock looking up at a starry blue sky" style="left:228px;top:31px;width:90px;height:130px;background:linear-gradient(#1a2a6a,#3a6ab0 60%,#0e1a3a)"></div>
    <div class="abs" style="left:299px;top:88px;width:28px;height:90px;background:linear-gradient(var(--violet),var(--indigo))"></div>
    <div class="diamond" style="left:18px;top:45px"></div>
    <div class="diamond" style="left:18px;top:79px"></div>
    <div class="diamond" style="left:18px;top:113px"></div>
    <div class="diamond" style="left:18px;top:147px"></div>
    <p class="abs body-copy" style="left:45px;top:46px;width:130px;font-size:5.4px;line-height:1.3">Lorem ipsum dolor sit amet, consectetur adipiscing elit, sed do eiusmod</p>
    <p class="abs body-copy" style="left:45px;top:80px;width:130px;font-size:5.4px;line-height:1.3">Lorem ipsum dolor sit amet, consectetur adipiscing elit, sed do eiusmod</p>
    <p class="abs body-copy" style="left:45px;top:114px;width:130px;font-size:5.4px;line-height:1.3">Lorem ipsum dolor sit amet, consectetur adipiscing elit, sed do eiusmod</p>
    <p class="abs body-copy" style="left:45px;top:148px;width:130px;font-size:5.4px;line-height:1.3">Lorem ipsum dolor sit amet, consectetur adipiscing elit, sed do eiusmod</p>
    <footer class="footer"><span class="page">Page No:<b>03</b></span><span class="url left">https://www.thelantern.org/</span><span class="mark">Lantern</span></footer>
  </section>

  <section class="slide c2 r3">
    <h2 class="heading right">Our Vision</h2>
    <div class="abs" style="left:0;top:0;width:24px;height:39px;background:linear-gradient(var(--violet-deep),var(--violet))"></div>
    <div class="abs" style="left:143px;top:92px;width:23px;height:84px;background:linear-gradient(var(--violet),var(--indigo))"></div>
    <div class="photo" role="img" aria-label="Cosmic artwork of hands reaching toward a glowing red nebula" style="left:9px;top:46px;width:149px;height:85px;border:1px solid #3a5aff;box-shadow:0 0 6px #3a5affaa;background:radial-gradient(circle at 50% 40%,#ff3a6a 0%,#a01a4a 25%,#2a0a2a 60%,#0a0a1a)"></div>
    <p class="abs body-copy" style="right:38px;top:46px;width:118px;text-align:right;font-size:5.4px;line-height:1.3">Lorem ipsum dolor sit amet, consectetur adipiscing elit, sed do eiusmod</p>
    <p class="abs body-copy" style="right:38px;top:78px;width:118px;text-align:right;font-size:5.4px;line-height:1.3">Lorem ipsum dolor sit amet, consectetur adipiscing elit, sed do eiusmod</p>
    <p class="abs body-copy" style="right:38px;top:109px;width:118px;text-align:right;font-size:5.4px;line-height:1.3">Lorem ipsum dolor sit amet, consectetur adipiscing elit, sed do eiusmod</p>
    <p class="abs body-copy" style="right:38px;top:141px;width:118px;text-align:right;font-size:5.4px;line-height:1.3">Lorem ipsum dolor sit amet, consectetur adipiscing elit, sed do eiusmod</p>
    <div class="chip" style="left:307px;top:44px"></div>
    <div class="chip" style="left:307px;top:76px"></div>
    <div class="chip" style="left:307px;top:107px"></div>
    <div class="chip" style="left:307px;top:139px"></div>
    <svg class="abs" style="left:307px;top:107px" width="15" height="15" viewBox="0 0 15 15"><ellipse cx="7.5" cy="7.5" rx="4.5" ry="2.8" fill="none" stroke="#fff" stroke-width="1"/><circle cx="7.5" cy="7.5" r="1.3" fill="#fff"/></svg>
    <footer class="footer"><span class="page">Page No:<b>04</b></span><span class="url">https://www.thelantern.org/</span><span class="mark">Lantern</span></footer>
  </section>

  <section class="slide c3 r3">
    <div class="photo" role="img" aria-label="Colourful nebula sky fading into purple" style="inset:0;background:radial-gradient(ellipse at 80% 10%,#3e7a6a 0%,transparent 40%),radial-gradient(ellipse at 15% 25%,#8a6a3a 0%,transparent 40%),linear-gradient(#3a3a38 0%,#4a3a5a 45%,#7a2fd0 55%,#4a1aa0 100%)"></div>
    <h2 class="heading center">Our Services</h2>
    <div class="card-dark" style="left:55px;top:41px;width:65px;height:102px">
      <svg width="12" height="9" viewBox="0 0 12 9"><circle cx="6" cy="2.5" r="2" fill="#fff"/><circle cx="2.5" cy="3.5" r="1.5" fill="#fff"/><circle cx="9.5" cy="3.5" r="1.5" fill="#fff"/><path d="M2 9a4 4 0 0 1 8 0z" fill="#fff"/></svg>
      <h4>Lorem Ipsum</h4>
      <p>Sed ut perspiciatis unde omnis iste natus error sit voluptatem accusantium doloremque laudantium, totam rem aperiam, eaque ipsa quae ab illo inventore veritatis et quasi architecto beatae vitae dicta sunt explicabo. Nemo enim ipsam voluptatem quia voluptas sit aspernatur aut</p>
    </div>
    <div class="card-dark" style="left:133px;top:41px;width:65px;height:102px">
      <svg width="12" height="9" viewBox="0 0 12 9"><path d="M1 5l3-3 2 1 2-1 3 3-3 3-2-1-2 1z" fill="none" stroke="#fff" stroke-width=".8"/></svg>
      <h4>Lorem Ipsum</h4>
      <p>Sed ut perspiciatis unde omnis iste natus error sit voluptatem accusantium doloremque laudantium, totam rem aperiam, eaque ipsa quae ab illo inventore veritatis et quasi architecto beatae vitae dicta sunt explicabo. Nemo enim ipsam voluptatem quia voluptas sit aspernatur aut</p>
    </div>
    <div class="card-dark" style="left:210px;top:41px;width:65px;height:102px">
      <svg width="12" height="9" viewBox="0 0 12 9"><path d="M3 8C3 4 6 1 10 1 10 5 7 8 3 8zM3 8l4-4" fill="none" stroke="#fff" stroke-width=".8"/></svg>
      <h4>Lorem Ipsum</h4>
      <p>Sed ut perspiciatis unde omnis iste natus error sit voluptatem accusantium doloremque laudantium, totam rem aperiam, eaque ipsa quae ab illo inventore veritatis et quasi architecto beatae vitae dicta sunt explicabo. Nemo enim ipsam voluptatem quia voluptas sit aspernatur aut</p>
    </div>
    <footer class="footer"><span class="page">Page No:<b>05</b></span><span class="url">https://www.thelantern.org/</span><span class="mark">Lantern</span></footer>
  </section>

  <section class="slide c1 r4">
    <h2 class="heading">The Problem</h2>
    <div class="photo" role="img" aria-label="Profile silhouette of a head filled with a pink galaxy and a question mark" style="left:161px;top:0;width:177px;height:180px;background:radial-gradient(ellipse at 60% 40%,#e0a0e8 0%,#b03aa8 25%,#4a1a5a 55%,#1c1c1e 80%)"></div>
    <svg class="abs" style="left:0;top:0" width="170" height="180" viewBox="0 0 170 180">
      <g fill="none" stroke="var(--orchid)" stroke-width="1">
        <polygon points="11,46 128,46 142,63 128,80 11,80"/>
        <polygon points="11,87 128,87 142,104 128,121 11,121"/>
        <polygon points="11,128 128,128 142,145 128,162 11,162"/>
      </g>
      <g fill="none" stroke="#fff" stroke-width="1">
        <circle cx="23" cy="62" r="4"/><line x1="26" y1="65" x2="29" y2="68"/>
        <circle cx="25" cy="104" r="6"/><line x1="25" y1="100" x2="25" y2="105"/>
        <circle cx="25" cy="143" r="4"/><line x1="23" y1="149" x2="27" y2="149"/>
      </g>
      <circle cx="25" cy="107.5" r=".7" fill="#fff"/>
    </svg>
    <div class="abs" style="left:34px;top:49px;width:94px">
      <div class="item-title">Lorem Ipsum</div>
      <p class="item-text">Lorem ipsum dolor sit amet, consectetur adipiscing elit, sed do</p>
    </div>
    <div class="abs" style="left:34px;top:90px;width:94px">
      <div class="item-title">Lorem Ipsum</div>
      <p class="item-text">Lorem ipsum dolor sit amet, consectetur adipiscing elit, sed do</p>
    </div>
    <div class="abs" style="left:34px;top:131px;width:94px">
      <div class="item-title">Lorem Ipsum</div>
      <p class="item-text">Lorem ipsum dolor sit amet, consectetur adipiscing elit, sed do</p>
    </div>
    <footer class="footer"><span class="page">Page No:<b>06</b></span><span class="url left">https://www.thelantern.org/</span><span class="mark">Lantern</span></footer>
  </section>

  <section class="slide c2 r4">
    <h2 class="heading">The Solution</h2>
    <div class="abs" style="left:24px;top:41px;width:137px;height:32px;border-radius:3px;background:linear-gradient(90deg,var(--magenta),var(--violet-deep))"></div>
    <div class="abs" style="left:184px;top:85px;width:137px;height:31px;border-radius:3px;background:linear-gradient(90deg,var(--magenta),var(--violet-deep))"></div>
    <div class="abs" style="left:18px;top:119px;width:143px;height:31px;border-radius:3px;background:linear-gradient(90deg,var(--violet-deep),var(--magenta))"></div>
    <div class="photo" role="img" aria-label="Illustration of a light bulb filled with a golden galaxy" style="left:134px;top:40px;width:68px;height:112px;background:radial-gradient(ellipse at 50% 35%,#b89050 0%,#7a5a34 45%,#3a2a26 100%)"></div>
    <div class="abs" style="left:45px;top:43px;width:100px">
      <div class="item-title">Lorem Ipsum</div>
      <p class="item-text">Lorem ipsum dolor sit amet, consectetur adipiscing elit, sed do</p>
    </div>
    <div class="abs" style="left:214px;top:87px;width:100px">
      <div class="item-title">Lorem Ipsum</div>
      <p class="item-text">Lorem ipsum dolor sit amet, consectetur adipiscing elit, sed do</p>
    </div>
    <div class="abs" style="left:45px;top:121px;width:84px">
      <div class="item-title">Lorem Ipsum</div>
      <p class="item-text">Lorem ipsum dolor sit amet, consectetur adipiscing elit, sed do</p>
    </div>
    <svg class="abs" style="left:29px;top:50px" width="12" height="12" viewBox="0 0 12 12"><circle cx="6" cy="6" r="4.5" fill="none" stroke="#fff" stroke-width=".8"/></svg>
    <svg class="abs" style="left:191px;top:94px" width="12" height="12" viewBox="0 0 12 12"><circle cx="6" cy="6" r="4.5" fill="none" stroke="#fff" stroke-width=".8"/></svg>
    <svg class="abs" style="left:26px;top:128px" width="12" height="12" viewBox="0 0 12 12"><path d="M6 1v10M1 6h10" stroke="#fff" stroke-width=".8"/></svg>
    <footer class="footer"><span class="page">Page No:<b>07</b></span><span class="url">https://www.thelantern.org/</span><span class="mark">Lantern</span></footer>
  </section>

  <section class="slide c3 r4" style="background:linear-gradient(#0e0d1a,#131220)">
    <h2 class="heading">Our Provided Services</h2>
    <div class="abs" style="left:16px;top:50px;width:141px;height:44px;background:linear-gradient(90deg,var(--violet-deep),var(--orchid))"></div>
    <div class="abs" style="left:175px;top:50px;width:140px;height:44px;background:linear-gradient(90deg,var(--violet-deep),var(--orchid))"></div>
    <div class="abs" style="left:16px;top:104px;width:141px;height:45px;background:linear-gradient(90deg,var(--violet-deep),var(--orchid))"></div>
    <div class="abs" style="left:175px;top:104px;width:140px;height:45px;background:linear-gradient(90deg,var(--violet-deep),var(--orchid))"></div>
    <svg class="abs" style="left:0;top:0" width="338" height="190" viewBox="0 0 338 190">
      <g fill="#fff"><circle cx="37" cy="72" r="15"/><circle cx="196" cy="72" r="15"/><circle cx="37" cy="127" r="15"/><circle cx="196" cy="127" r="15"/></g>
      <circle cx="37" cy="72" r="6" fill="none" stroke="#111" stroke-width="1.4"/>
      <circle cx="196" cy="72" r="6" fill="#111"/>
      <circle cx="37" cy="122" r="4" fill="#111"/><path d="M29 135a8 7 0 0 1 16 0z" fill="#111"/>
      <circle cx="196" cy="127" r="6" fill="none" stroke="#111" stroke-width="1.2"/>
    </svg>
    <div class="abs" style="left:58px;top:52px;width:92px">
      <div class="item-title">Lorem Ipsum</div>
      <p class="item-text" style="font-size:4.8px;line-height:1.3">Lorem ipsum dolor sit amet, consectetur adipiscing elit, sed do eiusmod</p>
    </div>
    <div class="abs" style="left:217px;top:52px;width:92px">
      <div class="item-title">Lorem Ipsum</div>
      <p class="item-text" style="font-size:4.8px;line-height:1.3">Lorem ipsum dolor sit amet, consectetur adipiscing elit, sed do eiusmod</p>
    </div>
    <div class="abs" style="left:58px;top:107px;width:92px">
      <div class="item-title">Lorem Ipsum</div>
      <p class="item-text" style="font-size:4.8px;line-height:1.3">Lorem ipsum dolor sit amet, consectetur adipiscing elit, sed do eiusmod</p>
    </div>
    <div class="abs" style="left:217px;top:107px;width:92px">
      <div class="item-title">Lorem Ipsum</div>
      <p class="item-text" style="font-size:4.8px;line-height:1.3">Lorem ipsum dolor sit amet, consectetur adipiscing elit, sed do eiusmod</p>
    </div>
    <footer class="footer"><span class="page">Page No:<b>08</b></span><span class="url">https://www.thelantern.org/</span><span class="mark">Lantern</span></footer>
  </section>

  <section class="slide c2 r5">
    <h2 class="heading">Our Partners</h2>
    <div class="abs" style="left:15px;top:52px;width:303px;height:15px;background:linear-gradient(90deg,var(--indigo),var(--violet) 70%,var(--orchid))"></div>
    <div class="abs" style="left:15px;top:52px;width:18px;height:91px;background:linear-gradient(var(--violet-deep),var(--indigo))"></div>
    <div class="abs" style="left:178px;top:126px;width:138px;height:16px;background:linear-gradient(90deg,var(--violet-deep),var(--orchid))"></div>
    <div class="tile" style="left:42px;top:33px;background:linear-gradient(135deg,#3a2a7a,#1a1a4a)"><span style="width:22px;height:4px;background:#ffffff99"></span></div>
    <div class="tile" style="left:111px;top:33px"><span style="width:26px;height:26px;border-radius:50%;background:#2ec45a"></span></div>
    <div class="tile" style="left:181px;top:33px"><span style="width:26px;height:26px;background:#c9a44a"></span></div>
    <div class="tile" style="left:251px;top:33px"><span style="width:38px;height:38px;border-radius:50%;background:#5aa8d0"></span></div>
    <div class="tile" style="left:42px;top:105px;background:#eeeeef"><span style="width:20px;height:20px;border-radius:50%;background:#2a9aa8"></span></div>
    <div class="tile" style="left:111px;top:105px;background:linear-gradient(135deg,#2a3a5a,#4a5a7a)"><span style="width:14px;height:14px;border-radius:50%;background:#5a3ad8"></span></div>
    <div class="tile" style="left:181px;top:105px;background:#e8e8e2"><span style="width:30px;height:30px;background:#7a9a8a"></span></div>
    <footer class="footer"><span class="page">Page No:<b>09</b></span><span class="url">https://www.thelantern.org/</span><span class="mark">Lantern</span></footer>
  </section>

</main>
</body>
</html>
```